make a fireworks website

we are manufacturer of fireworks in Asia.
we need a HD fireworks website for showing product to all world customers.
we also need an register for member system,location, forum,products..etc
I added my Logo for the company.
brightnova.com.hk

and please message me if you have
any question.
here some example of website:
http://www.skyplumeshow.com/
http://www.tornelupyro.com/
http://www.quarvel-pyro.co.uk/
http://www.mirethpyro.co.uk/

```html
<!DOCTYPE html>
<html lang="en">
<head>
<meta charset="utf-8">
<title>BrightNova Fireworks</title>
<link href="https://fonts.googleapis.com/css2?family=Carlito:ital,wght@0,400;0,700;1,400&display=swap" rel="stylesheet">
<style>
:root{
  --black:#000;
  --ink:#1e1e1e;
  --purple:#5b2d8c;
  --purple-dark:#3d1e63;
  --magenta:#b1174f;
  --frame:#d25b8a;
  --yellow:#f2e300;
  --pink:#e0145c;
  --white:#fff;
  --grey:#bdbdbd;
  --box:#2b2b2b;
}
*{margin:0;padding:0;box-sizing:border-box}
html,body{width:874px;height:1200px;overflow:hidden;background:var(--black)}
body{position:relative;font-family:"Carlito",Calibri,sans-serif;color:var(--white)}
.abs{position:absolute}
/* header */
.hero{left:0;top:0;width:874px;height:358px;background:var(--black);overflow:hidden}
.hero-photo{left:300px;top:58px;width:574px;height:300px;
  background:radial-gradient(ellipse at 55% 30%,#f6c24a 0,#a85a1a 18%,rgba(20,30,120,.9) 40%,#0b0f3a 65%,#000 90%)}
.util{top:10px;right:63px;display:flex;gap:22px;font-size:9px;color:#ddd}
.nav{left:304px;top:32px;width:570px;height:26px;background:var(--purple);display:flex;align-items:center;padding-left:28px;gap:12px;font-size:9px}
.search{margin-left:20px;width:122px;height:18px;background:#ddd;color:#777;font-size:8px;padding:4px 6px;display:flex;justify-content:space-between;align-items:center}
.brand{left:62px;top:62px;display:flex;align-items:center;gap:10px}
.brand-dot{width:60px;height:60px;border-radius:50%;background:var(--pink)}
.brand-name{font-size:30px;color:#ccc}
.hero-text{left:73px;top:196px;font-style:italic}
.hero-text .l1{font-size:22px;color:var(--yellow)}
.hero-text .l2{font-size:14px;margin-top:8px}
.hero-text .l3{font-size:22px;color:var(--pink);margin-top:6px}
.arrow{top:167px;width:36px;height:36px;border-radius:50%;background:#111;border:1px solid #333}
.offer-badge{left:672px;top:288px;width:132px;height:90px;border-radius:66px 66px 0 0;background:rgba(91,45,140,.45)}
.offer-inner{left:690px;top:304px;width:98px;height:70px;border-radius:49px 49px 0 0;background:var(--purple);text-align:center;font-style:italic;padding-top:18px}
.offer-inner .g{font-size:10px}.offer-inner .o{font-size:18px}
.strip{left:0;top:358px;width:874px;height:12px;background:var(--purple)}
/* special offers */
.offers{left:0;top:370px;width:874px;height:256px;background:var(--magenta)}
.offers h2{position:absolute;left:54px;top:26px;font-size:18px;font-weight:400}
.view-all{position:absolute;left:726px;top:30px;font-size:9px;color:var(--yellow)}
.product{position:absolute;top:72px;width:147px;text-align:center;font-size:9px}
.product .pic{height:128px;border:4px solid var(--frame);background:linear-gradient(135deg,#2a2f55,#6b3f2a 60%,#1a1a1a)}
.product .price{margin-top:9px}.product .name{margin-top:5px}
/* info */
.col{top:666px;width:200px;font-size:9.6px;line-height:16.4px;color:#ddd}
.col h3{font-size:15px;font-weight:400;color:var(--white);margin-bottom:10px;line-height:18px}
.col p{margin-bottom:16px}
.item{background:var(--box);height:21px;margin-bottom:5.5px;padding:3px 12px;font-size:9px;width:193px}
.more{color:var(--yellow)}
/* footer */
.footer{left:0;top:948px;width:874px;height:228px;background:var(--ink)}
.tweets{left:63px;top:962px;width:220px;font-size:9px;line-height:16.4px;color:#aaa}
.tweets h3{font-size:15px;font-weight:400;color:var(--white);margin-bottom:14px}
.tweets .at{color:var(--yellow);margin:6px 0 26px}
.divider{left:329px;top:972px;width:1px;height:180px;background:#333}
.signup-title{left:386px;top:970px;font-size:15px}
.signup-field{left:545px;top:966px;width:143px;height:24px;background:#f2f2f2}
.signup-btn{left:688px;top:966px;width:57px;height:24px;background:var(--purple);font-size:8.5px;text-align:center;line-height:24px}
.contact{left:388px;top:1011px;font-size:13px;line-height:32px}
.social{top:1025px;width:24px;height:24px;border-radius:50%;background:#2e2e2e;border:1px solid #444}
.foot-brand{left:392px;top:1086px;display:flex;align-items:center;gap:6px;font-size:14px;color:#888}
.foot-brand i{width:20px;height:20px;border-radius:50%;background:var(--pink)}
.card{top:1112px;width:46px;height:28px;border-radius:3px;background:#e8e8e8}
.bottom{left:0;top:1176px;width:874px;height:24px;background:var(--purple);font-size:9px;padding:7px 90px}
</style>
</head>
<body>
<header class="abs hero">
  <div class="abs hero-photo" role="img" aria-label="Photograph of golden and blue fireworks bursting over a night sky"></div>
  <nav class="abs util"><span>Whis List(0)</span><span>My Account</span><span>Shopping Cart</span><span>Checkout</span></nav>
  <nav class="abs nav"><span>HOME</span><span>LOCATIONS</span><span>OUR PRODUCTS</span><span>OFFERS</span><span>ABOUT US</span><span>REGISTER/LOGIN</span>
    <div class="search">SEARCH<svg width="10" height="10" viewBox="0 0 10 10"><circle cx="4" cy="4" r="3" fill="none" stroke="#5b2d8c" stroke-width="1.4"/><line x1="6" y1="6" x2="9.5" y2="9.5" stroke="#5b2d8c" stroke-width="1.6"/></svg></div>
  </nav>
  <div class="abs brand"><span class="brand-dot"></span><span class="brand-name">brightnova.com.hk</span></div>
  <div class="abs hero-text"><div class="l1">LIGHT UP</div><div class="l2">YOUR SPECIAL EVENT WITH OUR RANGE OF SPECIALLY</div><div class="l3">SELECTED FIREWORKS.</div></div>
  <div class="abs arrow" style="left:11px"><svg width="36" height="36"><path d="M21 11 L13 18 L21 25Z" fill="#999"/></svg></div>
  <div class="abs arrow" style="left:824px"><svg width="36" height="36"><path d="M15 11 L23 18 L15 25Z" fill="#999"/></svg></div>
  <div class="abs offer-badge"></div>
  <div class="abs offer-inner"><div class="g">GREAT</div><div class="o">OFFER</div></div>
</header>
<div class="abs strip"></div>
<section class="abs offers">
  <h2>SPECIAL OFFERS</h2>
  <span class="view-all">VIEW ALL PRODUCTS &gt;</span>
  <div class="product" style="left:54px"><div class="pic" role="img" aria-label="Product box of a firework cake"></div><div class="price">$350</div><div class="name">42S NOVA BURST</div></div>
  <div class="product" style="left:264px"><div class="pic" role="img" aria-label="Product box of a firework cake"></div><div class="price">$350</div><div class="name">42S NOVA BURST</div></div>
  <div class="product" style="left:472px"><div class="pic" role="img" aria-label="Illustrated product box of a firework cake"></div><div class="price">$350</div><div class="name">42S NOVA BURST</div></div>
  <div class="product" style="left:670px"><div class="pic" role="img" aria-label="Product box of a firework cake"></div><div class="price">$350</div><div class="name">42S NOVA BURST</div></div>
</section>
<section class="abs col" style="left:63px">
  <h3>WE HAVE THE FULL PACKAGE</h3>
  <p>Proin gravida nibh vel velit auctor aliquet. Aenean sollicitudin, lorem quis bibendum auctor, nisi elit consequat ipsum, nec sagittis sem nibh id elit.</p>
  <p>Duis sed odio sit amet nibh vulputate cursus a sit amet mauris. Morbi accumsan ipsum velit. Nam</p>
  <div class="item">Lorem quis bibendum auctor</div><div class="item">Lorem quis bibendum auctor</div><div class="item">Lorem quis bibendum auctor</div>
</section>
<section class="abs col" style="left:335px">
  <h3>SALE AT FANTASTIC PRICES</h3>
  <p>Proin gravida nibh vel velit auctor aliquet. Aenean sollicitudin, lorem quis bibendum auctor, nisi elit consequat ipsum, nec sagittis sem nibh id elit.</p>
  <p>Duis sed odio sit amet nibh vulputate cursus a sit amet mauris. Morbi accumsan ipsum velit. Nam nec tellus a odio tincidunt auctor a ornare odio.</p>
  <p>Sed non &nbsp;mauris vitae erat consequat auctor eu in elit. Class aptent taciti sociosqu ad litora torquent<br><span class="more">read more &gt;</span></p>
</section>
<section class="abs col" style="left:599px">
  <h3>REASON FOR CHOOSING US</h3>
  <p>Proin gravida nibh vel velit auctor aliquet. Aenean sollicitudin, lorem quis bibendum auctor, nisi elit consequat ipsum, nec sagittis sem nibh id elit.</p>
  <p>Duis sed odio sit amet nibh vulputate cursus a sit amet mauris. Morbi accumsan ipsum velit. Nam</p>
  <div class="item">Lorem quis bibendum auctor</div><div class="item">Lorem quis bibendum auctor</div><div class="item">Lorem quis bibendum auctor</div>
</section>
<footer class="abs footer"></footer>
<div class="abs tweets">
  <h3>LATEST TWEETS</h3>
  <div>liquet aenean sollicitudin, lorem quis bibendum ctor, nisi elit consequat ipsum, nec sagittis m”nibh id elit. Duis sed odio sit amet nibh vulputate cursus</div>
  <div class="at">@sollicitudin</div>
  <div>liquet aenean sollicitudin, lorem quis bibendum ctor, nisi elit consequat ipsum, nec sagittis m”nibh id elit. Duis sed odio sit amet nibh vulputate cursus</div>
  <div class="at">@sollicitudin</div>
</div>
<div class="abs divider"></div>
<div class="abs signup-title">OFFERS AND SPECIALS</div>
<div class="abs signup-field"></div>
<div class="abs signup-btn">SIGNUP</div>
<div class="abs contact">PHONE:&nbsp; (222) 555-0147<br>EMAIL:&nbsp; hello@brightnova-mail.com</div>
<span class="abs social" style="left:563px"></span>
<span class="abs social" style="left:594px"></span>
<span class="abs social" style="left:626px"></span>
<span class="abs social" style="left:662px"></span>
<div class="abs foot-brand"><i></i>BrightNova</div>
<span class="abs card" style="left:506px"></span>
<span class="abs card" style="left:558px"></span>
<span class="abs card" style="left:610px"></span>
<span class="abs card" style="left:664px"></span>
<div class="abs bottom">© 2014.&nbsp; All rights reserved. Terms of Service &amp; Privacy Policy.</div>
</body>
</html>
```